Brightwell Giving Inc

We need a full re-design of our non-profit organization website (www.brightwellgiving.org). Ideally, we are looking to make it more attractive, user-friendly, and interactive with our business model.

Please make sure to user colors that ago with our logo.

We need a homepage done and we also need a content page done where we will use for the other pages to fill with content.

Target Market(s)

Clothes/textiles donations.

Industry/Entity Type

Charity

Number of Pages Required

2 page

Colors

Designer to choose colors to be used in the design.

Requirements
Must have
• It must match the styling of our logo and same colors as current website. (www.brightwellgiving.org)
Nice to have
• Sleek homepage that is easy to understand and get our main points across.

```html
<!DOCTYPE html>
<html lang="en">
<head>
<meta charset="utf-8">
<title>Brightwell Giving – How it works</title>
<link rel="stylesheet" href="https://fonts.googleapis.com/css2?family=Poppins:wght@400;500;600;700&family=Dosis:wght@400;500;700&display=swap">
<style>
:root{
  --green:#1e7a1c;
  --green-text:#23841f;
  --yellow:#f8c22c;
  --ink:#2b2b2b;
  --field:#ececec;
  --white:#ffffff;
  --map-a:#eae6dc;
  --map-b:#d9e6cf;
}
*{box-sizing:border-box;margin:0;padding:0}
html,body{width:1200px;height:2956px;overflow:hidden;background:var(--white)}
body{position:relative;font-family:"Poppins",sans-serif;color:var(--ink)}
.abs{position:absolute}

/* header */
.brand{left:118px;top:38px;display:flex;align-items:center;gap:14px}
.brand-mark{width:60px;height:60px;border-radius:50%;background:var(--green)}
.brand-name{font-size:27px;font-weight:600;color:var(--green);letter-spacing:1px;line-height:1}
.brand-tag{font-size:12px;color:var(--green);margin-top:6px}

.finder{text-align:center}
.finder-title{font-size:15px;color:var(--ink)}
.finder-title b{font-weight:700}
.search{display:flex;margin-top:12px;border:1px solid var(--green);height:28px}
.search span{flex:1;font-size:11px;color:#888;padding:5px 8px;text-align:left;background:var(--white)}
.search i{width:40px;background:var(--green);display:flex;align-items:center;justify-content:center}
.finder-top{left:906px;top:30px;width:174px}

.nav{left:0;top:130px;width:1200px;height:60px;background:var(--green);display:flex;align-items:center;justify-content:space-between;padding:0 120px 0 122px}
.nav a{color:var(--white);font-size:16px;text-decoration:none}
.nav a.current{color:var(--yellow)}

/* steps */
.page-title{left:0;width:1200px;top:236px;text-align:center;font-size:28px;font-weight:600}
.step-head{left:0;width:1200px;text-align:center;font-size:29px;font-weight:500}
.step-head em{font-style:normal;color:var(--green-text)}
.step-body{left:262px;width:678px;text-align:center;font-size:17.5px;line-height:22.6px}
.step-body p+p{margin-top:28px}
.step-num{left:150px;width:40px;height:40px;border-radius:50%;background:var(--green);color:var(--white);font-weight:600;font-size:19px;display:flex;align-items:center;justify-content:center}

.intro{left:138px;width:924px;top:1284px;text-align:center;font-family:"Dosis",sans-serif;font-size:23.5px;line-height:33px;font-weight:500}
.intro b{font-weight:700}
.intro .name{color:var(--green-text)}

.finder-mid{left:516px;top:1548px;width:198px}
.map{left:142px;top:1670px;width:918px;height:631px;background:linear-gradient(135deg,var(--map-a),var(--map-b) 60%,var(--map-a))}

/* footer */
.footer{left:0;top:2354px;width:1200px;height:602px;background:var(--green);border-top:3px solid #e3a521;color:var(--white)}
.footer-title{left:0;width:1200px;top:58px;text-align:center;font-size:33px;font-weight:700}
.foot-nav{left:140px;top:104px}
.foot-nav h3{font-size:19px;font-weight:600;margin-bottom:14px}
.foot-nav a{display:block;color:var(--white);font-size:15px;font-weight:600;text-decoration:none;line-height:42.5px}
.foot-nav a.current{color:var(--yellow)}
.form{left:469px;top:100px;width:315px}
.field{background:var(--field);height:40px;margin-bottom:11px;font-size:16px;color:#999;padding:9px 12px}
.field.message{height:202px;margin-bottom:20px}
.submit{background:var(--yellow);height:49px;color:#3a3a3a;font-size:21px;text-align:center;line-height:49px}
.offices{right:140px;top:104px;text-align:right}
.offices h4{font-size:18px;font-weight:600;margin-bottom:10px}
.offices p{font-size:13.5px;line-height:20px;margin-bottom:16px}
.badges{right:140px;top:440px;display:flex;gap:12px}
.badges span{width:44px;height:50px;background:var(--yellow);border-radius:4px}
</style>
</head>
<body>

<header>
  <div class="abs brand">
    <div class="brand-mark"></div>
    <div>
      <div class="brand-name">BRIGHTWELL GIVING</div>
      <div class="brand-tag">Think Globally while Donating Locally</div>
    </div>
  </div>
  <div class="abs finder finder-top">
    <div class="finder-title">Find a <b>Donation</b> Place</div>
    <div class="search"><span>Search location</span><i><svg width="16" height="16" viewBox="0 0 16 16"><circle cx="7" cy="7" r="5" fill="none" stroke="#fff" stroke-width="2"/><line x1="11" y1="11" x2="15" y2="15" stroke="#fff" stroke-width="2"/></svg></i></div>
  </div>
  <nav class="abs nav">
    <a>Home</a><a>Missions</a><a class="current">How it works</a><a>About Us</a><a>Sponsors</a><a>News</a><a>Donate</a><a>Wall of Needs</a>
  </nav>
</header>

<main>
  <h1 class="abs page-title">How it works</h1>

  <h2 class="abs step-head" style="top:304px"><em>Drop off</em> clothing at your closest donation bin.</h2>
  <div class="abs step-num" style="top:390px">1</div>
  <div class="abs step-body" style="top:362px">
    <p>We have different collection procedures. For outdoors we can place a donation bin, a metal container about 48"L X 48"WX86"H. Inside collecting we would use a commercial laundry bin 48"LX29"WX55"H. We can also schedule pick up of donated clothing, where we would supply a plastic bag and the donated clothing would be left. Outside or in dryway for a scheduled pick up.</p>
  </div>

  <h2 class="abs step-head" style="top:546px"><em>We pick it</em> up and take it to our sorting facility.</h2>
  <div class="abs step-num" style="top:713px">2</div>
  <div class="abs step-body" style="top:598px">
    <p>After our drivers pick up the clothing from our designated donation locations, the items are taken to our sorting facility where they are separated into three categories. Ten percent of the clothing is designated as category A which is higher-end pieces that are like-new or only slightly used.</p>
    <p>These items are sold to second-hand and vintage clothing stores. The remaining 90% are separated into categories B and C. Category B clothing are items that are in used condition but can be resold in thrift stores once they are washed. This comprises approximately 40% of our donations. The remaining clothing, category C, are items that are not able to be resold in thrift stores. These pieces are sold to non-profit organizations overseas for resale in foreign markets.</p>
  </div>

  <h2 class="abs step-head" style="top:950px">Charities get clothing. <em>We pay you</em> for the clothes.</h2>
  <div class="abs step-num" style="top:1119px">3</div>
  <div class="abs step-body" style="top:1014px">
    <p>Once we are done distributing our donated clothing to their appropriate channels, the proceeds from the sales are distributed in two ways. The first distribution is in the form of donations to local charities and benevolent organizations.</p>
    <p>The majority of our proceeds from sales are used in this manner. The rest of the proceeds are used for Brightwell Giving's operating costs. Some of these costs include our pickup drivers, truck maintenance, and sort facility staff. This allows us to function as an organization and continue to help those who need it most.</p>
  </div>

  <p class="abs intro">Recycling your <b>old clothing</b> is a significant humanitarian act. <span class="name">Brightwell Giving</span> works towards simplifying the collection process by providing practical solutions for waste reduction. <span class="name">Brightwell Giving</span> is particularly qualified to assure an effort for an outstanding clothing recovery initiative. "If your organization is a church, community center, an educational facility or a fitness center", we can arrange for your clothing drop boxes to be placed in your facility, get the word out about the "clothing collection event; retain the clothing afterwards," and distribute the donations to the proper channels, so minimal amount goes to waste.</p>

  <div class="abs finder finder-mid">
    <div class="finder-title">Find a <b>Donation</b> Place</div>
    <div class="search"><span>Search location</span><i><svg width="16" height="16" viewBox="0 0 16 16"><circle cx="7" cy="7" r="5" fill="none" stroke="#fff" stroke-width="2"/><line x1="11" y1="11" x2="15" y2="15" stroke="#fff" stroke-width="2"/></svg></i></div>
  </div>
  <div class="abs map" role="img" aria-label="Map of the region marking donation bin locations"></div>
</main>

<footer class="abs footer">
  <h2 class="abs footer-title">Contact Us</h2>
  <div class="abs foot-nav">
    <h3>Navigation</h3>
    <a>Home</a><a class="current">Missions</a><a>How it Works</a><a>About Us</a><a>Sponsors</a><a>News</a><a>Donate</a><a>Wall of Needs</a>
  </div>
  <form class="abs form">
    <div class="field">Full Name</div>
    <div class="field">Company</div>
    <div class="field">Email</div>
    <div class="field message">Message</div>
    <div class="submit">Submit</div>
  </form>
  <div class="abs offices">
    <h4>New York Office</h4>
    <p>42 Orchard Ln<br>Ashford NY 12098<br>(555) 410-8836</p>
    <h4>NY Warehouse</h4>
    <p>1190 Ridge Rd<br>Millbrook<br>NY 12399</p>
    <h4>Thrift Store</h4>
    <p>76 Elmwood Ave<br>Linden<br>NY 12577</p>
  </div>
  <div class="abs badges"><span></span><span></span><span></span></div>
</footer>

</body>
</html>
```